Re-design my 1-page website to be BETTER!

Hi Guys,
I recently created a 1-page website for market testing purposes for a company I am starting. Problem is, the feedback i've had on the page is its a bit corporate and boring.
I would love you to design something that is fresher, more modern and will generate leads (via the sign up CTA's).
Here is the website as it is now: www.guidelinkhub.com.au.
If you need any info or have questions, just reach out.
Thanks,
Oliver

Target Market(s)

Entrepreneurs

Number of Pages Required

1 page

Font styles to use
Sans Serif

Colors
abd036
34a6d7
ffffff

Requirements
Must have
• Fresh, Modern, high-converting
• I expect 70% of traffic to be mobile so must be mobile optimised first.
Nice to have
• I've highlighted colours i like below, however, I am open to suggestions. I like colours that are gender neutral and show energy and vibrancy.
• I have used Proxima Nova for the fonts, as I find it easy to read however, I am open to suggestions. My main preference is that it displays well and is easily read

```html
<!DOCTYPE html>
<html lang="en">
<head>
<meta charset="UTF-8">
<title>GuideLink Hub – A Mentor For Everyone</title>
<link href="https://fonts.googleapis.com/css2?family=Montserrat:wght@300;400;500;600;700;800&display=swap" rel="stylesheet">
<style>
  :root {
    --wood-dark: #2b1a10;
    --wood-mid: #4a2e1d;
    --wood-light: #5c3b26;
    --white: #ffffff;
    --leaf: #709628;
    --leaf-bright: #3be23b;
    --accent-green: #2f8f12;
    --ink: #15241c;
    --muted: #6f7478;
    --body: #3b3f42;
    --sky: #d3e0e6;
    --badge: #2a6e9e;
    --device-tone: #8a9a78;
    --cap-tone: #b9c3c8;
  }
  * { box-sizing: border-box; margin: 0; padding: 0; }
  html, body { width: 1110px; height: 1200px; overflow: hidden; }
  body { font-family: "Montserrat", sans-serif; background: var(--sky); position: relative; }

  .hero {
    position: absolute; left: 0; top: 0; width: 1110px; height: 539px;
    background: linear-gradient(100deg, var(--wood-dark) 0%, var(--wood-mid) 40%, var(--wood-light) 60%, var(--wood-mid) 80%, var(--wood-dark) 100%);
    overflow: hidden; color: var(--white);
  }
  .hero-kicker {
    position: absolute; top: 21px; left: 0; width: 100%; text-align: center;
    font-size: 18px; font-weight: 500; letter-spacing: 0.3px;
  }
  .hero-quote {
    position: absolute; left: 192px; top: 86px; width: 720px;
    font-size: 21px; font-weight: 300; line-height: 39px; letter-spacing: 0.5px;
  }
  .hero-attribution {
    position: absolute; left: 192px; top: 240px;
    font-size: 21px; font-weight: 300; letter-spacing: 0.5px;
  }
  .hero-attribution .name { color: var(--leaf-bright); font-weight: 400; }
  .btn {
    position: absolute; top: 339px; height: 65px; border-radius: 33px;
    display: flex; align-items: center; justify-content: center;
    font-size: 21px; font-weight: 700; letter-spacing: 0.3px; text-decoration: none;
  }
  .btn-find { left: 283px; width: 250px; background: var(--leaf); color: var(--ink); }
  .btn-search { left: 575px; width: 252px; border: 2px solid var(--leaf); color: var(--white); }
  .device-visual {
    position: absolute; left: 60px; top: 300px; width: 150px; height: 262px;
    border-radius: 22px;
    background: linear-gradient(160deg, #a9ab9c, var(--device-tone));
    opacity: 0.85;
    transform: rotate(33deg);
  }
  .notepad-visual {
    position: absolute; left: 945px; top: 200px; width: 210px; height: 270px;
    background: var(--white); transform: rotate(-30deg);
  }

  .features {
    position: absolute; left: 0; top: 539px; width: 1110px; height: 661px;
    background: var(--sky);
  }
  .features-title {
    position: absolute; left: 310px; top: 70px;
    font-size: 33px; font-weight: 800; letter-spacing: 1.6px; color: var(--ink);
  }
  .features-title .hl { color: var(--accent-green); }
  .features-lede {
    position: absolute; left: 312px; top: 108px;
    font-size: 15px; line-height: 24px; color: var(--muted); letter-spacing: -0.6px; font-weight: 500;
  }
  .cap-visual {
    position: absolute; left: 830px; top: 46px; width: 105px; height: 112px;
    border-radius: 14px;
    background: linear-gradient(160deg, var(--cap-tone), rgba(185,195,200,0.4));
  }
  .step {
    position: absolute; top: 222px; width: 240px; text-align: center;
  }
  .step-badge {
    width: 166px; height: 166px; border-radius: 50%; background: var(--badge);
    margin: 0 auto; display: flex; align-items: center; justify-content: center;
  }
  .step-title {
    margin-top: 20px; font-size: 18px; font-weight: 600; letter-spacing: 0.6px; color: var(--ink);
  }
  .step-text {
    margin: 6px auto 0; width: 210px; font-size: 14px; line-height: 29px; color: var(--body); font-weight: 500;
  }
  .step-need { left: 96px; }
  .step-choose { left: 436px; }
  .step-support { left: 768px; }
</style>
</head>
<body>
  <header class="hero">
    <div class="device-visual" role="img" aria-label="Photo of a smartphone lying on a wooden desk"></div>
    <div class="notepad-visual" role="img" aria-label="Photo of a spiral notepad with a pencil on the desk"></div>

    <p class="hero-kicker">A Mentor For Everyone</p>
    <blockquote class="hero-quote">"We've flipped the model on its head -&nbsp; so now you choose your Mentor.&nbsp; It's never been this easy to get the advice and guidance you need to thrive"</blockquote>
    <p class="hero-attribution"><span class="name">Oliver, Founder</span> - GuideLink Hub</p>

    <a class="btn btn-find" href="#">Find Now</a>
    <a class="btn btn-search" href="#">Search Now</a>
  </header>

  <section class="features">
    <h2 class="features-title">Mentorship: But <span class="hl">Different</span></h2>
    <p class="features-lede">Finding a Mentor used to be hard; but not any more.<br>We've turned the traditional model on its head, so now Mentors seek you.</p>
    <div class="cap-visual" role="img" aria-label="Illustration of a graduation cap and diploma"></div>

    <article class="step step-need">
      <div class="step-badge">
        <svg width="90" height="90" viewBox="0 0 90 90" fill="none" stroke="#fff" stroke-width="4" stroke-linejoin="round" stroke-linecap="round">
          <path d="M14 40 L50 22 L58 66 L20 58 Z" fill="#fff"/>
          <path d="M22 58 L30 80"/>
          <path d="M66 30 L74 22 M68 44 L80 42 M66 56 L76 60"/>
        </svg>
      </div>
      <h3 class="step-title">Tell Us What You Need</h3>
      <p class="step-text">There is no one size fits all approach to Mentorship.&nbsp; So tell us the challenges you are facing and the skill-set your Mentor must have.</p>
    </article>

    <article class="step step-choose">
      <div class="step-badge">
        <svg width="90" height="100" viewBox="0 0 90 100" fill="none" stroke="#fff" stroke-width="4" stroke-linejoin="round" stroke-linecap="round">
          <path d="M34 60 V22 a6 6 0 0 1 12 0 V50 M46 46 a6 6 0 0 1 12 0 V54 M58 50 a6 6 0 0 1 12 0 V74 c0 10 -8 18 -18 18 H44 c-6 0 -10 -3 -14 -8 L16 66 a6 6 0 0 1 9 -8 L34 66"/>
          <path d="M28 22 a12 12 0 0 1 24 0 M22 22 a18 18 0 0 1 36 0"/>
        </svg>
      </div>
      <h3 class="step-title">Choose Your Mentor</h3>
      <p class="step-text">Mentors are invited to Mentor you. We select 3 top picks that align with your criteria.&nbsp; It's then up to you whether you choose a Mentor, interview 1 or more or refine your criteria and</p>
    </article>

    <article class="step step-support">
      <div class="step-badge">
        <svg width="100" height="90" viewBox="0 0 100 90" fill="none" stroke="#fff" stroke-width="4" stroke-linejoin="round" stroke-linecap="round">
          <circle cx="50" cy="34" r="20"/>
          <path d="M28 34 V28 a22 22 0 0 1 44 0 V34"/>
          <rect x="24" y="30" width="8" height="14" rx="3" fill="#fff"/>
          <rect x="68" y="30" width="8" height="14" rx="3" fill="#fff"/>
          <path d="M72 44 c0 8 -8 12 -16 12"/>
          <path d="M14 84 c0 -14 14 -22 36 -22 s36 8 36 22 Z"/>
        </svg>
      </div>
      <h3 class="step-title">Ongoing Support</h3>
      <p class="step-text">There is no one size fits all approach to Mentorship.&nbsp; So tell us the challenges you are facing and the skill-set your Mentor must have.</p>
    </article>
  </section>
</body>
</html>
```